Recruitment Agency in Texas, needs a stand out header letter

Our colours are red and grey and can be found on our website
just my logo will be sufficient and address...

Target Market(s)

Engineering Manufacturing

Colors
0094D4
00A9DD
6FCCEA
C7EBF8
E9F6FB
EB3D1F
EC4F4E
F09395
F8D3D4
FCEDEE

Requirements
Must have
• use colors red and grey
Should not have
• Please use same colors and font as my logo. My website is kelbrinstaffing.com

```html
<!DOCTYPE html>
<html lang="en">
<head>
<meta charset="utf-8">
<title>KelbrinStaffing Letterhead</title>
<link href="https://fonts.googleapis.com/css2?family=Open+Sans:wght@400;600&family=Roboto:wght@400&display=swap" rel="stylesheet">
<style>
  :root {
    --brand-red: #d71920;
    --brand-grey: #5f6064;
    --text-grey: #4d4d4d;
    --paper: #f8f8f8;
    --backdrop: #dcdcdc;
    --ink: #1a1a1a;
  }
  * { margin: 0; padding: 0; box-sizing: border-box; }
  html, body {
    width: 1153px; height: 1200px; overflow: hidden;
    background: var(--backdrop);
  }
  .letterhead {
    position: absolute;
    left: 160px; top: 20px;
    width: 832px; height: 1160px;
    background: var(--paper);
    box-shadow: 0 6px 18px rgba(0,0,0,0.12);
  }
  .brand-name {
    position: absolute;
    top: 88px; left: 0; width: 100%;
    text-align: center;
    font-family: "Open Sans", sans-serif;
    font-weight: 600;
    font-size: 52px;
    letter-spacing: -0.5px;
    color: var(--brand-red);
    line-height: 1;
  }
  .letter-body {
    position: absolute;
    left: 74px; top: 257px; width: 682px;
    font-family: "Open Sans", sans-serif;
    font-size: 15.6px;
    line-height: 22.4px;
    color: var(--text-grey);
  }
  .letter-body p { margin-bottom: 22.4px; text-align: justify; }
  .letter-body .salutation, .letter-body .closing { text-align: left; }
  .signature {
    position: absolute;
    left: 74px; top: 846px;
    width: 100px; height: 92px;
    background: linear-gradient(135deg, #e4e4e4, #cfcfcf);
  }
  .contact-footer {
    position: absolute;
    left: 0; top: 1027px; width: 100%;
    text-align: center;
    font-family: "Roboto", sans-serif;
    font-size: 18px;
    line-height: 25px;
    color: #2b2b2b;
  }
  .office-label { color: var(--brand-red); }
  .contact-icon {
    width: 16px; height: 14px;
    vertical-align: -1px;
    margin-right: 4px;
    fill: var(--brand-red);
  }
  .contact-item { margin-right: 6px; }
</style>
</head>
<body>
  <main class="letterhead">
    <div class="brand-name">KelbrinStaffing</div>

    <section class="letter-body">
      <p class="salutation">Dear customer,</p>
      <p>Lorem ipsum dolor sit amet, consectetur adipisicing elit, sed do eiusmod tempor incididunt ut labore et dolore magna aliqua. Ut enim ad minim veniam, quis nostrud exercitation ullamco laboris nisi ut aliquip ex ea commodo consequat. Duis aute irure dolor in reprehenderit in voluptate velit esse cillum dolore eu fugiat nulla pariatur. Excepteur sint occaecat cupidatat non proident, sunt in culpa qui officia deserunt mollit anim id est laborum.</p>
      <p>Lorem ipsum dolor sit amet, consectetur adipisicing elit, sed do eiusmod tempor incididunt ut labore et dolore magna aliqua. Ut enim ad minim veniam, quis nostrud exercitation ullamco laboris nisi ut aliquip ex ea commodo consequat. Duis aute irure dolor in reprehenderit in voluptate velit esse cillum dolore eu fugiat nulla pariatur. Excepteur sint occaecat cupidatat non proident, sunt in culpa qui officia deserunt mollit anim id est laborum.</p>
      <p>Lorem ipsum dolor sit amet, consectetur adipisicing elit, sed do eiusmod tempor incididunt ut labore et dolore magna aliqua. Ut enim ad minim veniam, quis nostrud exercitation ullamco laboris nisi ut aliquip ex ea commodo consequat. Duis aute irure dolor in reprehenderit in voluptate velit esse cillum dolore eu fugiat nulla pariatur. Excepteur sint occaecat cupidatat non proident, sunt in culpa qui officia deserunt mollit anim id est laborum.</p>
      <p>Lorem ipsum dolor sit amet, consectetur adipisicing elit, sed do eiusmod tempor incididunt ut labore et dolore magna aliqua. Ut enim ad minim veniam, quis nostrud exercitation ullamco laboris nisi ut aliquip ex ea commodo consequat. Duis aute irure dolor in reprehenderit.</p>
      <p class="closing">Yours Sincerely,</p>
    </section>

    <div class="signature" role="img" aria-label="Handwritten signature of the sender"></div>

    <footer class="contact-footer">
      <div><span class="office-label">Houston Office :</span> 48 Larkfield Avenue Houston</div>
      <div>
        <span class="contact-item">
          <svg class="contact-icon" viewBox="0 0 16 14" aria-hidden="true"><path d="M2 4c0-2 2-3 6-3s6 1 6 3v1h-3V4H5v1H2z M4 6h8l2 6H2z"/></svg>(+1) 555-014-2290
        </span>
        <span class="contact-item">
          <svg class="contact-icon" viewBox="0 0 16 14" aria-hidden="true"><path d="M4 1h8v3H4z M1 5h14v6h-3v-2H4v2H1z M5 10h6v4H5z"/></svg>555-014-2291
        </span>
        <span>
          <svg class="contact-icon" viewBox="0 0 16 14" aria-hidden="true"><path d="M1 2h14v10H1z" /><path d="M1 2l7 6 7-6" fill="none" stroke="#f8f8f8" stroke-width="1.4"/></svg>info@kelbrinstaffing.com
        </span>
      </div>
      <div>www.kelbrinstaffing.com</div>
    </footer>
  </main>
</body>
</html>
```